Young Architect Bussiness Card

English is not my first language (spanish is).
Need a bussiness card design for my best friend who is about to graduate from college, Licentiate degree in architecture, so she needs business cards to start networking, currently she has no porfolio, web page or facebook. so she is relying on her cel phone and gmail, but should leave space for one of them (facebook)

Design for business card should be modern, maybe something with construction blue prints patern or 3D modelling.

Name: Mariela Fonseca Arrieta
Licentiate in Arquitecture
Cel: (506) XXX-4827
email: marielaXXX@correovela.com

Services, although im not sure if it has to be there or not:
Anteproyectos / Proposal design
Inspecciones / Site Inspections
Modelado 3D / 3D modelling
Planos Constructivos / Construction Blue Prints
Presupuestos / Budgets

Design should be in spanish

Contact Information for Business Card

Name: Mariela Fonseca, Arquitecto
Associtation code : XXXX
Phone: (506) XXXX-XXXX
Email: xxx@correovela.com
Facebook: xxxx

Requirements
Must have
• Design for business card should be modern, maybe something with construction blue prints patern or 3D modelling.
Nice to have
• Something like a transition from 2D to 3D.

```html
<!DOCTYPE html>
<html lang="es">
<head>
<meta charset="UTF-8">
<title>Mariela Fonseca Arrieta — Tarjeta de presentación</title>
<link rel="stylesheet" href="https://fonts.googleapis.com/css2?family=Lato:wght@400;700&display=swap">
<style>
  :root {
    --stage: #2b2b2d;
    --card-white: #ffffff;
    --card-black: #050505;
    --ink: #1a1a1a;
    --ink-light: #f2f2f2;
    --accent: #f2d916;
    --accent-deep: #e3c80c;
    --accent-soft: #fff176;
  }
  * { box-sizing: border-box; margin: 0; padding: 0; }
  html, body {
    width: 1200px; height: 880px; overflow: hidden;
    background: var(--stage);
    font-family: "Lato", Arial, sans-serif;
  }
  .sheet {
    position: relative; width: 1200px; height: 880px;
    display: flex; flex-direction: column; align-items: center;
    justify-content: center; gap: 40px;
  }
  .card {
    position: relative; width: 700px; height: 400px;
    border-radius: 26px; overflow: hidden;
  }
  .card--front { background: var(--card-white); color: var(--ink); }
  .card--back { background: var(--card-black); color: var(--ink-light); }

  .cube-cluster { position: absolute; inset: 0; width: 700px; height: 400px; }

  .identity { position: absolute; left: 56px; top: 150px; z-index: 1; }
  .identity__name {
    font-size: 23px; font-weight: 400; letter-spacing: 0.4px;
    text-transform: uppercase; color: var(--accent);
  }
  .identity__title { font-size: 17px; margin-top: 2px; }

  .contact {
    position: absolute; left: 56px; bottom: 46px; z-index: 1;
    list-style: none; font-size: 19px; line-height: 1.3;
  }
  .contact__label { color: var(--accent-deep); }

  .services { position: absolute; left: 56px; bottom: 44px; z-index: 1; }
  .services__heading {
    font-size: 20px; font-weight: 700; color: var(--accent);
    margin-bottom: 6px; letter-spacing: 0.4px;
  }
  .services__list { list-style: none; font-size: 17px; line-height: 1.4; }
</style>
</head>
<body>
<main class="sheet">

  <section class="card card--front" aria-label="Frente de la tarjeta">
    <svg class="cube-cluster" viewBox="0 0 700 400" role="img" aria-label="Cúmulo de cubos amarillos en 3D flotando">
      <defs>
        <linearGradient id="cubeFrontFill" x1="0" y1="0" x2="1" y2="1">
          <stop offset="0" stop-color="var(--accent-soft)"/>
          <stop offset="1" stop-color="var(--accent-deep)"/>
        </linearGradient>
      </defs>
      <polygon points="560,0 700,0 700,250 630,330 540,320 470,270 455,200 470,140 410,105 430,65 500,30" fill="url(#cubeFrontFill)"/>
    </svg>

    <header class="identity">
      <h1 class="identity__name">Mariela Fonseca Arrieta</h1>
      <p class="identity__title">Licenciada en Arquitectura</p>
    </header>

    <ul class="contact">
      <li><span class="contact__label">Cel:</span> (506) XXX-4827</li>
      <li><span class="contact__label">Email:</span> marielaXXX@correovela.com</li>
    </ul>
  </section>

  <section class="card card--back" aria-label="Reverso de la tarjeta">
    <svg class="cube-cluster" viewBox="0 0 700 400" role="img" aria-label="Cúmulo de cubos amarillos en 3D flotando">
      <defs>
        <linearGradient id="cubeBackFill" x1="0" y1="0" x2="1" y2="1">
          <stop offset="0" stop-color="var(--accent-soft)"/>
          <stop offset="1" stop-color="var(--accent-deep)"/>
        </linearGradient>
      </defs>
      <polygon points="620,0 700,0 700,250 640,320 560,300 515,240 490,185 430,150 440,100 520,70 580,30" fill="url(#cubeBackFill)"/>
    </svg>

    <div class="services">
      <h2 class="services__heading">SERVICIOS</h2>
      <ul class="services__list">
        <li>Anteproyectos / Proposal design</li>
        <li>Inspecciones / Site Inspections</li>
        <li>Modelado 3D / 3D modelling</li>
        <li>Planos Constructivos / Construction Blue Prints</li>
        <li>Presupuestos / Budgets</li>
      </ul>
    </div>
  </section>

</main>
</body>
</html>
```